Design a menu for health restaurant

A health food restaurant in Los Angeles is seeking menu design. Our foods are made from scratch using whole ingredients.
Name: Grubb Larder
Address: 1000 E 60th StLos Angeles, CA 90247
Website: www.GrubbLarder.example
We are looking for a clean and simple menu. Brand colors are white/tan, green and orange.

Please see attached excel with menu items and logo. We do not yet have prices.

Colors
f78f20
9bcb3c
ffffff
fff3d1

Requirements
Must have
• Easy to read.
Trifold menu design (front and back).
VEGAN, VEGETARIAN, GLUTEN FREE, CONTAINS NUTS symbols.
Logo.
Nice to have
• Incorporate brand colors, but still be easy to read.
We would like to use the Belco font (attached) if it works. If not we are open to a similar font that is easy to read.

Please see attached images.
We like the images and headers of OPTION 1. Would like something similar in trifold format.
We like the clean fonts of OPTION 2.

```html
<!DOCTYPE html>
<html lang="en">
<head>
<meta charset="utf-8">
<title>Grubb Larder – Trifold Menu</title>
<link rel="stylesheet" href="https://fonts.googleapis.com/css2?family=Baloo+2:wght@700;800&family=Oswald:wght@500&family=Open+Sans:wght@400;600&display=swap">
<style>
  :root {
    --orange: #f78f20;
    --green: #9bcb3c;
    --cream: #fff3d1;
    --white: #ffffff;
    --ink: #3a3a3a;
  }
  * { box-sizing: border-box; margin: 0; padding: 0; }
  html, body { width: 1200px; height: 967px; overflow: hidden; background: var(--white); }
  body { position: relative; font-family: "Open Sans", sans-serif; color: var(--ink); }

  .sheet { position: absolute; left: 65px; top: 69px; width: 1080px; height: 839px; background: var(--cream); }
  .band { position: absolute; }
  .band--green { background: var(--green); }
  .band--orange { background: var(--orange); }

  .section-title {
    position: absolute; font-family: "Baloo 2", sans-serif; font-weight: 800;
    font-size: 20px; letter-spacing: 0.5px; text-transform: uppercase;
    color: #474747; line-height: 1;
  }

  .item { position: absolute; width: 150px; font-size: 10px; line-height: 1.35; }
  .item--wide { width: 162px; }
  .item__name {
    font-family: "Oswald", sans-serif; font-weight: 500; font-size: 11px;
    text-transform: uppercase; letter-spacing: 0.3px; color: #2f2f2f;
    display: flex; align-items: center; gap: 3px; flex-wrap: wrap;
  }
  .item__price { font-size: 9px; margin: 1px 0 4px; }
  .item__desc { color: #444; }

  .diet { display: inline-flex; align-items: center; justify-content: center;
    width: 11px; height: 11px; border: 1px solid #333; border-radius: 50%;
    font-family: "Open Sans", sans-serif; font-size: 5.5px; font-weight: 600; line-height: 1; }
  .diet--gf { width: 14px; border-radius: 3px; }

  .photo { position: absolute; }
  .photo--smoothies { left: 195px; top: 144px; width: 153px; height: 104px;
    background: linear-gradient(135deg, #f3a7a0, #e9503f 45%, #f59b32 75%, #c8d9e8); }
  .photo--cookies { left: 30px; top: 722px; width: 150px; height: 86px;
    background: linear-gradient(120deg, #e8e4dc, #5a3a28 35%, #c9a070 70%, #eceae4); }

  .brand { position: absolute; left: 797px; top: 150px; width: 200px; text-align: center; }
  .brand__mark { width: 100px; height: 100px; border-radius: 50%; background: var(--orange); margin: 0 auto 12px; }
  .brand__name { font-family: "Open Sans", sans-serif; font-weight: 600; font-size: 24px; color: var(--orange); }

  .dots { position: absolute; left: 715px; top: 560px; }

  .contact { position: absolute; left: 715px; top: 583px; width: 365px; height: 256px; background: var(--orange);
    color: var(--white); text-align: center; padding-top: 48px; }
  .contact__label { font-family: "Oswald", sans-serif; font-weight: 500; font-size: 11.5px; letter-spacing: 0.5px; }
  .contact__value { font-size: 14.5px; margin-bottom: 29px; }
</style>
</head>
<body>
<main class="sheet">
  <div class="band band--green" style="left:0;top:0;width:362px;height:38px"></div>
  <div class="band band--orange" style="left:362px;top:0;width:353px;height:38px"></div>
  <div class="band band--green" style="left:715px;top:0;width:365px;height:38px"></div>
  <div class="band band--orange" style="left:0;top:275px;width:362px;height:19px"></div>
  <div class="band band--green" style="left:0;top:514px;width:362px;height:20px"></div>
  <div class="band band--green" style="left:715px;top:518px;width:365px;height:30px"></div>

  <h2 class="section-title" style="left:30px;top:22px">Smoothies</h2>
  <div class="item" style="left:30px;top:62px">
    <div class="item__name">Green Machine Smoothie <span class="diet">V</span><span class="diet diet--gf">GF</span><span class="diet">N</span></div>
    <div class="item__price">11.99</div>
    <div class="item__desc">Romaine, spinach, banana, mango, pineapple, flaxmilk, spirulina, almond butter</div>
  </div>
  <div class="item" style="left:30px;top:160px">
    <div class="item__name">Acai Smoothie <span class="diet">V</span><span class="diet diet--gf">GF</span><span class="diet">N</span></div>
    <div class="item__price">11.99</div>
    <div class="item__desc">Acai, blueberries, banana, pineapple, Macqui berry, flaxmilk, almond butter</div>
  </div>
  <div class="item" style="left:195px;top:62px">
    <div class="item__name">Mango Smoothie</div>
    <div class="item__price">11.99 <span class="diet">V</span> <span class="diet diet--gf">GF</span></div>
    <div class="item__desc">Mango, flaxmilk, banana, hemp seeds</div>
  </div>
  <div class="photo photo--smoothies" role="img" aria-label="Photo of colourful smoothies in cups with straws"></div>

  <h2 class="section-title" style="left:30px;top:277px">Snacks N' Sides</h2>
  <div class="item" style="left:30px;top:312px">
    <div class="item__name">Fries <span class="diet">V</span><span class="diet diet--gf">GF</span></div>
    <div class="item__price">11.99</div>
    <div class="item__desc">Hand cut air-fries with house seasonings. Choose regular or sweet potato fries.</div>
  </div>
  <div class="item" style="left:30px;top:400px">
    <div class="item__name">Side Salad</div>
    <div class="item__price">11.99</div>
    <div class="item__desc">Your choice of House, Golden Beet, Mediterranean, or Vegan Chef side salad. (24oz) 11.99</div>
  </div>
  <div class="item" style="left:195px;top:312px">
    <div class="item__name">Guac + Chips <span class="diet">V</span><span class="diet diet--gf">GF</span></div>
    <div class="item__price">11.99</div>
    <div class="item__desc">Guacamole with blue corn tortilla chips.</div>
  </div>
  <div class="item" style="left:195px;top:388px">
    <div class="item__name">Hummus + Chips <span class="diet">V</span><span class="diet diet--gf">GF</span></div>
    <div class="item__price">11.99</div>
    <div class="item__desc">Hummus with blue corn tortilla chips.</div>
  </div>

  <h2 class="section-title" style="left:30px;top:517px">Desserts</h2>
  <div class="item" style="left:30px;top:566px">
    <div class="item__name">Date Coffee Cake <span class="diet">V</span><span class="diet diet--gf">GF</span></div>
    <div class="item__price">11.99</div>
    <div class="item__desc">Signature date coffee cake with walnuts.</div>
  </div>
  <div class="item" style="left:30px;top:640px">
    <div class="item__name">Fruit + Spices <span class="diet">V</span><span class="diet diet--gf">GF</span></div>
    <div class="item__price">11.99</div>
    <div class="item__desc">Strawberry, pineapple, green apple, orange, and blueberries with lime and chili seasoning.</div>
  </div>
  <div class="photo photo--cookies" role="img" aria-label="Photo of two baked chocolate chip cookies"></div>
  <div class="item" style="left:195px;top:566px">
    <div class="item__name">Cookies
      <svg width="10" height="9" viewBox="0 0 10 9" aria-hidden="true"><path d="M1 1 L5 8 L9 1" fill="none" stroke="#333" stroke-width="1.6"/></svg></div>
    <div class="item__price">11.99</div>
    <div class="item__desc">Your choice of Chocolate Chip or Double Chocolate Chip fresh baked cookie.</div>
  </div>
  <div class="item" style="left:195px;top:654px">
    <div class="item__name">Larder Chocolate Mousse <span class="diet">V</span><span class="diet diet--gf">GF</span></div>
    <div class="item__price">11.99</div>
    <div class="item__desc">Served with grated dark chocolate.</div>
  </div>

  <h2 class="section-title" style="left:373px;top:22px">Drinks</h2>
  <div class="item" style="left:372px;top:69px">
    <div class="item__name">Coffee</div>
    <div class="item__price">11.99</div>
    <div class="item__desc">We proudly serve Driftwood Coffee, a local roaster.</div>
  </div>
  <div class="item" style="left:372px;top:144px">
    <div class="item__name">Power Date Shake <span class="diet">V</span><span class="diet diet--gf">GF</span></div>
    <div class="item__price">11.99</div>
    <div class="item__desc">Ice-blended energy smoothie featuring dates and coffee.</div>
  </div>
  <div class="item" style="left:372px;top:220px">
    <div class="item__name">Heart Beet Juice <span class="diet">V</span><span class="diet diet--gf">GF</span></div>
    <div class="item__price">11.99</div>
    <div class="item__desc">Red beet, apple, carrot, ginger, parsley, and lemon.</div>
  </div>
  <div class="item" style="left:372px;top:295px">
    <div class="item__name">Green Leafy Juice <span class="diet">V</span><span class="diet diet--gf">GF</span></div>
    <div class="item__price">11.99</div>
    <div class="item__desc">Spinach, kale, cucumber, apple, and oranges.</div>
  </div>
  <div class="item" style="left:372px;top:371px">
    <div class="item__name">Orange Turmeric Juice <span class="diet">V</span><span class="diet diet--gf">GF</span></div>
    <div class="item__price">11.99</div>
    <div class="item__desc">Turmeric, ginger, lemon, carrot, and orange topped with cracked black pepper.</div>
  </div>
  <div class="item" style="left:372px;top:459px">
    <div class="item__name">Fireshot <span class="diet">V</span><span class="diet diet--gf">GF</span></div>
    <div class="item__price">11.99</div>
    <div class="item__desc">Ginger and lemon shot topped with cayenne.</div>
  </div>
  <div class="item item--wide" style="left:543px;top:69px">
    <div class="item__name">Lemonade</div>
    <div class="item__price">11.99</div>
    <div class="item__desc">House Made Lemonade. Choice of unsweetened or agave sweetened in Regular, Raspberry, and Lavender flavors.</div>
  </div>
  <div class="item item--wide" style="left:543px;top:176px">
    <div class="item__name">Tea</div>
    <div class="item__price">11.99</div>
    <div class="item__desc">Hot or iced.</div>
  </div>
  <div class="item item--wide" style="left:543px;top:238px">
    <div class="item__name">Bottled Drinks</div>
    <div class="item__price">11.99</div>
    <div class="item__desc">
      <p>Verde kombucha<br>(Berry Blend, Ginger Citrus, Golden Peach)</p>
      <p style="margin-top:5px">Fizzwell<br>(Orange Mango, Lemon, Grapefruit)</p>
      <p style="margin-top:5px">Palm Grove Coconut Original</p>
      <p style="margin-top:5px">Sparkling Water<br>(Clearwell)</p>
      <p style="margin-top:5px">Still Water (Clearwell)</p>
    </div>
  </div>

  <div class="brand">
    <div class="brand__mark"></div>
    <div class="brand__name">Grubb Larder</div>
  </div>

  <svg class="dots" width="365" height="8" viewBox="0 0 365 8" aria-hidden="true">
    <line x1="6" y1="4" x2="362" y2="4" stroke="#9bcb3c" stroke-width="5" stroke-linecap="round" stroke-dasharray="0 16.2"/>
  </svg>

  <section class="contact">
    <div class="contact__label">PHONE</div>
    <div class="contact__value">(555) 014-2290</div>
    <div class="contact__label">EMAIL</div>
    <div class="contact__value">Info@GrubbLarder.example</div>
    <div class="contact__label">ORDER ONLINE</div>
    <div class="contact__value">www.GrubbLarder.example</div>
  </section>
</main>
</body>
</html>
```